Homebuilder & Remodeling Firm looking for archectrual looking website

We are a Custom home building & remodeling company since 1986 and would like to launch a website.Tom Halvery the principle of the firm is a graduate of Marlow Univesity school of architecture and draws his own designs and working drawings. and has done many residential, single and multi family projects in the Dallas Ft Worth Metroplex. We want our website to be architectural in design and visually appealing. We will eventually have photos to provide for you. The message we want to communicate is we have current update knowledge with trends, and longevity in experience. Our message is that we are a firm that designs and remodels fully through and we provide a well executed custom home that is unique to each client. The Homes that we build are unique ,authentic and sustainable architectural styles such as mid century modern, contemporary, transitional and they are sophisticated homes to compliment individual lifestyles of our clients. We have a passion for construction and an attention to detail that makes your dreams come to life. We listen to each clients every need in functionality and form and take them from pre-construction to post-construction follow -up.
We help you invest in your home. Thoughts Create Reality

EXAMPLES OF WEBSITES THAT WE LIKE. PLEASE DO
MORE CONTEMPORARY, SLEEK, ARCHITECTURAL

* Please make the LOGO a bigger part of design

http://penwickgroup.build/
https://www.quillorn.co/
http://vantrelmodernhomes.com/
http://www.neilcorradesign.com/
http://www.fennickolde.com/
http://ravodesignstudios.com/about
http://mendaleigc.com/

thank you,

Reason: We have many clients asking to see our website and re ready to launch something for them to look at

Target Market(s)

Home owners, home buyers, interior designers, All ages

Industry/Entity Type

Builders

Coding

Coded - Design and coding required

Number of Pages Required

5+ page

Font styles to use
Sans Serif

Requirements
Must have
• HTML5 OR PHP
• graphic artist must speak English:
• *Visually appealing, user friendly,
• * the website should reflect the stability and integrity of the company since it has been in business for over 30 years
• * a sophistication and refinement is our mandate.
Should not have
• Too busy, too much going on, we want more minimal in design and artsitic

```html
<!DOCTYPE html>
<html lang="en">
<head>
<meta charset="utf-8">
<title>Halvery Development — Custom Homes &amp; Remodeling</title>
<link href="https://fonts.googleapis.com/css2?family=Montserrat:wght@300;400;600&display=swap" rel="stylesheet">
<style>
  :root{
    --navy:#1d2d5c;
    --ink:#333333;
    --nav-bg:#f4f4f5;
    --white:#ffffff;
    --line:#5a5a5a;
    --copy:#555555;
  }
  *{margin:0;padding:0;box-sizing:border-box}
  html,body{width:830px;height:1200px;overflow:hidden;background:var(--white)}
  body{font-family:"Montserrat",sans-serif;color:var(--ink);position:relative}

  .site-nav{position:absolute;top:0;left:0;width:830px;height:34px;background:var(--nav-bg);z-index:5}
  .site-nav a{position:absolute;top:12px;font-size:12px;font-weight:400;color:var(--ink);text-decoration:none}
  .site-nav a.is-active{color:var(--navy);font-weight:600}

  .panel{position:absolute;left:0;width:830px;overflow:hidden}
  .panel svg.panel-art{position:absolute;top:0;left:0}
  .panel-hero{top:34px;height:380px}
  .panel-interiors{top:414px;height:381px}
  .panel-commercial{top:795px;height:379px}

  .brand{position:absolute;left:46px;top:33px;width:220px;display:flex;flex-direction:column;align-items:center}
  .brand-square{width:62px;height:62px;background:var(--navy)}
  .brand-name{margin-top:40px;font-size:17px;font-weight:400;color:var(--navy);letter-spacing:.1px;white-space:nowrap}

  .panel-title{position:absolute;font-size:18px;font-weight:300;line-height:23px;color:var(--ink);text-transform:uppercase;white-space:nowrap;letter-spacing:-.1px}
  .panel-copy{position:absolute;width:203px;font-size:6.3px;line-height:8.7px;text-transform:uppercase;text-align:justify;color:var(--copy);letter-spacing:.15px}
  .btn-more{position:absolute;width:68px;height:24px;border:1px solid var(--line);background:rgba(255,255,255,.7);font-size:9px;font-weight:300;color:var(--ink);display:flex;align-items:center;justify-content:center;text-decoration:none}

  .slider-dots{position:absolute;left:49px;top:329px;display:flex;gap:4px}
  .slider-dots span{width:9.5px;height:9.5px;border-radius:50%;border:1px solid #555;background:var(--white)}
  .slider-dots span.is-current{background:var(--navy);border-color:var(--navy)}

  .site-footer{position:absolute;top:1184px;left:0;width:830px;text-align:center;font-size:7px;color:#444}
</style>
</head>
<body>

<nav class="site-nav">
  <a class="is-active" href="#" style="left:185px">HOME</a>
  <a href="#" style="left:248px">PORTFOLIO</a>
  <a href="#" style="left:352px">SERVICES</a>
  <a href="#" style="left:436px">PROCESS</a>
  <a href="#" style="left:520px">ABOUT</a>
  <a href="#" style="left:583px">CONTACT</a>
</nav>

<section class="panel panel-hero">
  <svg class="panel-art" width="830" height="380" viewBox="0 0 830 380">
    <defs>
      <linearGradient id="heroSky" x1="0" y1="0" x2="0" y2="1">
        <stop offset="0" stop-color="#c4d6ea"/>
        <stop offset=".28" stop-color="#ecebe6"/>
        <stop offset=".5" stop-color="#4c4f55"/>
        <stop offset=".66" stop-color="#8a8680"/>
        <stop offset=".8" stop-color="#2f8f93"/>
        <stop offset="1" stop-color="#9a9c9c"/>
      </linearGradient>
      <linearGradient id="heroShade" x1="0" y1="0" x2="1" y2="0">
        <stop offset="0" stop-color="#c89a6f" stop-opacity=".45"/>
        <stop offset=".35" stop-color="#ffffff" stop-opacity="0"/>
        <stop offset="1" stop-color="#2a2c30" stop-opacity=".25"/>
      </linearGradient>
    </defs>
    <g role="img" aria-label="Photo of a modern two-storey white villa with a pool and sun loungers">
      <rect x="205" y="0" width="625" height="380" fill="url(#heroSky)"/>
      <rect x="205" y="0" width="625" height="380" fill="url(#heroShade)"/>
    </g>
    <polygon points="205,0 350,0 300,140 415,260 300,380 205,380" fill="#ffffff" opacity=".72"/>
    <polygon points="205,0 260,0 415,260 300,380 205,380" fill="#ffffff" opacity=".45"/>
    <polygon points="300,380 415,260 380,380" fill="#ffffff" opacity=".35"/>
  </svg>

  <div class="brand">
    <div class="brand-square"></div>
    <div class="brand-name">HALVERY DEVELOPMENT</div>
  </div>

  <h1 class="panel-title" style="left:47px;top:209px">Lorem ipsum<br>dolor sit amet, consectetur.</h1>
  <a class="btn-more" href="#" style="left:49px;top:276px">READ MORE</a>
  <div class="slider-dots"><span></span><span class="is-current"></span><span></span><span></span><span></span><span></span></div>
</section>

<section class="panel panel-interiors">
  <svg class="panel-art" width="830" height="381" viewBox="0 0 830 381">
    <defs>
      <linearGradient id="interiorWalls" x1="0" y1="0" x2="1" y2="0">
        <stop offset="0" stop-color="#6a4a30"/>
        <stop offset=".08" stop-color="#b9aa98"/>
        <stop offset=".2" stop-color="#e2e2e0"/>
        <stop offset=".45" stop-color="#d2d6d8"/>
        <stop offset=".62" stop-color="#b7a38a"/>
        <stop offset=".8" stop-color="#e9ecee"/>
        <stop offset="1" stop-color="#cfd5da"/>
      </linearGradient>
      <linearGradient id="interiorFloor" x1="0" y1="0" x2="0" y2="1">
        <stop offset="0" stop-color="#ffffff" stop-opacity=".15"/>
        <stop offset=".55" stop-color="#ffffff" stop-opacity="0"/>
        <stop offset=".75" stop-color="#8a6a4a" stop-opacity=".35"/>
        <stop offset="1" stop-color="#2e2a28" stop-opacity=".6"/>
      </linearGradient>
    </defs>
    <g role="img" aria-label="Photo of a bright remodeled kitchen with glass cabinets and a wood counter">
      <rect x="0" y="0" width="675" height="381" fill="url(#interiorWalls)"/>
      <rect x="0" y="0" width="675" height="381" fill="url(#interiorFloor)"/>
    </g>
    <polygon points="480,0 675,0 675,381 450,381 430,260" fill="#ffffff" opacity=".55"/>
    <polygon points="545,0 675,0 675,381 470,381 580,260 490,0" fill="#ffffff" opacity=".5"/>
  </svg>

  <h2 class="panel-title" style="left:496px;top:172px">Lorem ipsum<br>dolor sit amet, consectetur.</h2>
  <p class="panel-copy" style="left:598px;top:231px">Lorem ipsum dolor sit amet, consectetur adipiscing elit. Nullam elementum libero sit amet velit egestas egestas. Quisque velit ante, blandit quis accumsan eu, elementum a tortor. Nunc ultrices risus sit amet ultrices ultrices. Aenean maximus nisi a dui lobortis placerat. Suspendisse pretium, tortor at vehicula inter-</p>
  <a class="btn-more" href="#" style="left:599px;top:300px">READ MORE</a>
</section>

<section class="panel panel-commercial">
  <svg class="panel-art" width="830" height="379" viewBox="0 0 830 379">
    <defs>
      <radialGradient id="towerSky" cx=".55" cy=".55" r=".6">
        <stop offset="0" stop-color="#cfe2f4"/>
        <stop offset=".25" stop-color="#5f9ee0"/>
        <stop offset=".6" stop-color="#23528f"/>
        <stop offset="1" stop-color="#0f2452"/>
      </radialGradient>
      <linearGradient id="towerGlass" x1="0" y1="0" x2="1" y2="1">
        <stop offset="0" stop-color="#0d1f4a" stop-opacity=".5"/>
        <stop offset=".5" stop-color="#0d1f4a" stop-opacity="0"/>
        <stop offset="1" stop-color="#0d1f4a" stop-opacity=".55"/>
      </linearGradient>
    </defs>
    <g role="img" aria-label="Photo looking up at glass office towers against a blue sky">
      <rect x="142" y="0" width="688" height="379" fill="url(#towerSky)"/>
      <rect x="142" y="0" width="688" height="379" fill="url(#towerGlass)"/>
    </g>
    <polygon points="142,0 350,0 310,110 415,250 380,379 142,379" fill="#f2f3f6" opacity=".85"/>
    <polygon points="200,0 260,0 415,250 225,379 142,379 142,120" fill="#ffffff" opacity=".35"/>
  </svg>

  <h2 class="panel-title" style="left:31px;top:181px">Lorem ipsum<br>dolor sit amet, consectetur.</h2>
  <p class="panel-copy" style="left:30px;top:240px">Lorem ipsum dolor sit amet, consectetur adipiscing elit. Nullam elementum libero sit amet velit egestas egestas. Quisque velit ante, blandit quis accumsan eu, elementum a tortor. Nunc ultrices risus sit amet ultrices ultrices. Aenean maximus nisi a dui lobortis placerat. Suspendisse pretium, tortor at vehicula inter-</p>
  <a class="btn-more" href="#" style="left:31px;top:307px">READ MORE</a>
</section>

<footer class="site-footer">COPYRIGHT 2017 | ALL RIGHTS RESERVED</footer>

</body>
</html>
```